Narvelo - Human Capital Consultancy Business Cards

We need a business card design for a new professional services consulting company which is focused on People, Performance, Profit. Hence the company name "Narvelo Pty Ltd". We intend to work with organisations predominantly on achieving optimal business performance through it's people. Developing both individual and organisational capability through effective learning and talent management strategies. We also plan to offer leadership programs which look at how people can utilise wellness, mindfulness and resilience to enable them and their teams to perform more effectively. We are looking for something quite dynamic, even sporty looking rather than a staid'professional services' look. Please see logo attached.

Leadership

```html
<!DOCTYPE html>
<html lang="en">
<head>
<meta charset="utf-8">
<title>Narvelo Pty Ltd – Business Cards</title>
<link rel="stylesheet" href="https://fonts.googleapis.com/css2?family=Source+Sans+3:wght@400;600&display=swap">
<style>
  :root {
    --navy: #0a3a8f;
    --navy-deep: #062a72;
    --navy-light: #1146a8;
    --red: #e0301e;
    --orange: #f07a1a;
    --grey: #8a8b8d;
    --ink: #222;
    --paper: #ffffff;
    --backdrop: #3a3a3a;
  }
  html, body {
    margin: 0;
    width: 1200px;
    height: 900px;
    overflow: hidden;
    background: var(--backdrop);
    font-family: "Source Sans 3", "Myriad Pro", Arial, sans-serif;
  }
  p, h1, ul { margin: 0; }
  .canvas { position: relative; width: 1200px; height: 900px; }
  .card {
    position: absolute;
    top: 308px;
    width: 515px;
    height: 285px;
    box-shadow: 0 4px 14px rgba(0,0,0,.45);
    overflow: hidden;
  }
  .sep { margin: 0 4px; font-size: 11px; vertical-align: 2px; }
  .tagline { font-size: 16px; line-height: 20px; white-space: nowrap; }

  /* Front */
  .card--front {
    left: 72px;
    background: radial-gradient(ellipse at 45% 30%, var(--navy-light), var(--navy) 55%, var(--navy-deep));
    color: var(--paper);
    text-align: center;
  }
  .front-brand {
    position: absolute;
    top: 105px;
    left: 0;
    right: 0;
    display: flex;
    justify-content: center;
    align-items: center;
    gap: 12px;
    font-weight: 600;
    font-size: 52px;
    line-height: 60px;
    letter-spacing: 1px;
  }
  .front-brand .dot { width: 30px; height: 30px; border-radius: 50%; background: var(--paper); }
  .card--front .tagline { position: absolute; top: 236px; left: 0; right: 0; }

  /* Back */
  .card--back { left: 615px; background: var(--paper); }
  .band { position: absolute; left: 0; top: 0; }
  .holder { position: absolute; left: 29px; top: 36px; }
  .holder-name { font-weight: 400; font-size: 25px; color: var(--navy); line-height: 30px; }
  .holder-role { margin-top: 2px; font-size: 17px; line-height: 22px; color: var(--red); }
  .contacts {
    position: absolute;
    left: 29px;
    top: 152px;
    padding: 0;
    list-style: none;
    font-size: 14px;
    color: var(--ink);
    line-height: 18px;
  }
  .contacts li { display: flex; align-items: center; gap: 5px; }
  .contacts svg { width: 11px; height: 11px; fill: var(--red); }
  .back-brand-name {
    position: absolute;
    right: 28px;
    top: 62px;
    width: 210px;
    display: flex;
    justify-content: center;
    align-items: center;
    gap: 8px;
    font-weight: 600;
    font-size: 42px;
    line-height: 50px;
    color: var(--grey);
  }
  .back-brand-name .dot { width: 26px; height: 26px; border-radius: 50%; background: var(--orange); }
  .card--back .tagline {
    position: absolute;
    right: 28px;
    top: 180px;
    width: 210px;
    text-align: center;
    color: var(--ink);
    font-size: 14.5px;
  }
  .website {
    position: absolute;
    left: 0;
    right: 0;
    top: 250px;
    text-align: center;
    color: var(--paper);
    font-size: 14px;
    line-height: 18px;
  }
</style>
</head>
<body>
<main class="canvas">
  <section class="card card--front" aria-label="Card front">
    <div class="front-brand"><span class="dot"></span><span>Narvelo</span></div>
    <p class="tagline">Talent<span class="sep">•</span>Growth<span class="sep">•</span>Results</p>
  </section>

  <section class="card card--back" aria-label="Card back">
    <svg class="band" width="515" height="285" viewBox="0 0 515 285">
      <path d="M70 234 Q300 240 515 200 L515 213 Q300 244 70 234 Z" fill="var(--red)"/>
      <path d="M0 228 Q280 252 515 214 L515 285 L0 285 Z" fill="var(--navy)"/>
    </svg>

    <div class="holder">
      <h1 class="holder-name">Daniel Harrow</h1>
      <p class="holder-role">managing director</p>
    </div>

    <ul class="contacts">
      <li><svg viewBox="0 0 12 12"><path d="M3 1 L5 3.5 L4 5 Q5 7 7 8 L8.5 7 L11 9 L9.5 11 Q5 11 1 6.5 Q1 2.5 3 1 Z"/></svg>555 214 36 90</li>
      <li><svg viewBox="0 0 12 12"><path d="M1 3 H11 V10 H1 Z M1 3 L6 7 L11 3" stroke="#fff" stroke-width=".8"/></svg>info@narvelo.com</li>
      <li><svg viewBox="0 0 12 12"><rect x="1" y="1" width="10" height="10" rx="1.5"/></svg>@narvelo</li>
    </ul>

    <div class="back-brand-name"><span class="dot"></span><span>Narvelo</span></div>
    <p class="tagline">Talent<span class="sep">•</span>Growth<span class="sep">•</span>Results</p>

    <p class="website">www.narvelo.com</p>
  </section>
</main>
</body>
</html>
```